I need a business card designed using the logo provided either vertical or horizontal......Tallowmere Advisory is an Australian based real estate company that caters for the upper end of the market so the design of the business card "must reflect" the companies image!!
Colour combinations are optional but "must be realistic" and must be able to be accurately useable CMYK colours.
Please consider that any colours used "must be able to be used" and be suitable in following designs for "pull out banner signs" and "real estate signs".
The colours and the font in the attached designs are for example and other combinations are encouraged.
Target Market(s)
The High End of the Australian real estate market
Industry/Entity Type
Business
Contact Information for Business Card
Logo - Business Name - Director + Licensed Real Estate Agent - Mobile Number (Cell Phone) - Business Number - Fax - Email Address - Web address
Requirements
Must have
- Designs and colours (CMYK) that can easily be interpreted by an Australian printer.
Nice to have
- Some alternative ideas on colour and font..........the ones provided are ok and have been provided as an example but I am looking for alternative ideas
Should not have
- Loud, overly bright colours. Designs that do not reflect the professional standards of the business.
- Designs that look good on a computer monitor but can not be re-created on a printing press.............this is most important when it comes to shading etc.

```html
<!DOCTYPE html>
<html lang="en">
<head>
<meta charset="utf-8">
<title>Tallowmere Advisory – Business Card</title>
<link rel="stylesheet" href="https://fonts.googleapis.com/css2?family=Open+Sans:wght@400;600;700&display=swap">
<style>
  :root {
    --backdrop: #e4e4e4;
    --card: #ffffff;
    --gold-deep: #b87b2b;
    --gold-soft: #d3c48f;
    --ink: #1d1d1d;
    --ink-muted: #3a3a3a;
    --paper-text: #ffffff;
  }
  * { box-sizing: border-box; margin: 0; padding: 0; }
  html, body {
    width: 1200px; height: 852px; overflow: hidden;
    background: var(--backdrop);
    font-family: "Open Sans", Arial, sans-serif;
  }
  .sheet {
    width: 1200px; height: 852px;
    display: flex; align-items: center; justify-content: center; gap: 48px;
  }
  .card {
    position: relative;
    width: 540px; height: 310px;
    background: var(--card);
    border-radius: 22px;
    overflow: hidden;
    box-shadow: 0 4px 14px rgba(0,0,0,0.18);
  }

  /* Brand lockup: name in one colour and weight with one plain square */
  .brand { display: flex; align-items: center; gap: 14px; }
  .brand-mark { width: 18px; height: 18px; background: var(--gold-deep); flex: none; }
  .brand-name {
    font-weight: 700; color: var(--ink);
    text-transform: uppercase; letter-spacing: 3px; line-height: 1.15;
  }

  /* Front */
  .card-front { display: flex; align-items: center; justify-content: center; }
  .card-front .brand-name { font-size: 30px; }

  /* Back */
  .card-back .bands { position: absolute; inset: 0; }
  .card-back .brand { position: absolute; left: 70px; top: 40px; }
  .card-back .brand-mark { width: 16px; height: 16px; }
  .card-back .brand-name { font-size: 22px; letter-spacing: 2.5px; }
  .rule { position: absolute; height: 1.5px; }
  .rule-top { left: 360px; top: 98px; width: 150px; background: linear-gradient(90deg, var(--gold-deep), transparent); }
  .rule-bottom { left: 50px; top: 200px; width: 160px; background: linear-gradient(90deg, transparent, var(--gold-deep)); }
  .person { position: absolute; left: 0; width: 440px; top: 112px; text-align: center; }
  .person-name { font-size: 17px; font-weight: 700; color: var(--ink); }
  .person-title { font-size: 12.5px; color: var(--ink-muted); }
  .contacts {
    position: absolute; left: 22px; bottom: 14px;
    list-style: none; color: var(--paper-text); font-size: 13px; line-height: 20px;
  }
  .contacts li { display: flex; align-items: center; gap: 8px; }
  .contacts svg { width: 12px; height: 12px; fill: var(--paper-text); flex: none; }
  .website {
    position: absolute; right: 20px; top: 183px;
    font-size: 12px; color: var(--ink);
  }
</style>
</head>
<body>
<main class="sheet">

  <section class="card card-front" aria-label="Card front">
    <div class="brand">
      <span class="brand-mark"></span>
      <span class="brand-name">Tallowmere Advisory</span>
    </div>
  </section>

  <section class="card card-back" aria-label="Card back">
    <svg class="bands" viewBox="0 0 540 310" aria-hidden="true">
      <polygon points="0,222 260,222 282,168 380,168 340,310 0,310" fill="var(--gold-deep)"/>
      <polygon points="380,168 540,168 540,310 340,310" fill="var(--gold-soft)"/>
    </svg>

    <div class="brand">
      <span class="brand-mark"></span>
      <span class="brand-name">Tallowmere Advisory</span>
    </div>
    <span class="rule rule-top"></span>

    <div class="person">
      <p class="person-name">Harriet Calloway</p>
      <p class="person-title">Managing Director</p>
    </div>
    <span class="rule rule-bottom"></span>

    <ul class="contacts">
      <li>
        <svg viewBox="0 0 24 24"><path d="M6.6 10.8a15 15 0 0 0 6.6 6.6l2.2-2.2c.3-.3.7-.4 1-.2 1.1.4 2.3.6 3.6.6.6 0 1 .4 1 1V20c0 .6-.4 1-1 1A17 17 0 0 1 3 4c0-.6.4-1 1-1h3.5c.6 0 1 .4 1 1 0 1.3.2 2.5.6 3.6.1.3 0 .7-.2 1z"/></svg>
        <span>000 0 0 000 00</span>
        <svg viewBox="0 0 24 24"><path d="M6 3h9v5H6zM4 9h16v9H4zm3 3v2h10v-2zM7 19h10v2H7z"/></svg>
        <span>(03) 5550 4172</span>
      </li>
      <li>
        <svg viewBox="0 0 24 24"><path d="M2 5h20v14H2zm2 2v.5l8 5 8-5V7z"/></svg>
        <span>harriet@tallowmere.com.au</span>
      </li>
      <li>
        <svg viewBox="0 0 24 24"><path d="M12 2a7 7 0 0 0-7 7c0 5 7 13 7 13s7-8 7-13a7 7 0 0 0-7-7zm0 9.5A2.5 2.5 0 1 1 12 6.5a2.5 2.5 0 0 1 0 5z"/></svg>
        <span>Your long commercial of office address</span>
      </li>
    </ul>

    <p class="website">www.tallowmere.com.au</p>
  </section>

</main>
</body>
</html>
```